International wholesale business needs a business card

We need a business card.

Company Details:
Company Name and logo
Address, Phone number, Website
Employee Details:
Name, Designation, Mobile Number & Email address

Logo file is attached.

```html
<!DOCTYPE html>
<html lang="en">
<head>
<meta charset="utf-8">
<title>Kestrel Trading – Business Card</title>
<link rel="stylesheet" href="https://fonts.googleapis.com/css2?family=Poppins:wght@400;500;700&display=swap">
<style>
  :root {
    --bg: #ececec;
    --brand-red: #bf2632;
    --slate: #878d94;
    --paper: #f5f5f4;
    --white: #ffffff;
    --ink-grey: #7d8187;
  }
  * { margin: 0; padding: 0; box-sizing: border-box; }
  html, body { width: 1200px; height: 721px; overflow: hidden; background: var(--bg); }
  body { font-family: "Poppins", sans-serif; position: relative; }

  .card {
    position: absolute;
    top: 212px;
    width: 520px;
    height: 297px;
    overflow: hidden;
    box-shadow: 0 10px 24px rgba(0,0,0,0.12);
  }

  /* Personal side */
  .card--personal { left: 55px; background: var(--slate); }
  .card__shape { position: absolute; inset: 0; width: 100%; height: 100%; }
  .person-name {
    position: absolute; left: 34px; top: 30px;
    color: var(--white); font-weight: 700; font-size: 22px;
    line-height: 1.1; letter-spacing: 2px; text-transform: uppercase;
  }
  .person-role {
    position: absolute; left: 300px; top: 118px;
    color: var(--white); font-weight: 500; font-size: 10px;
    letter-spacing: 4px; text-transform: uppercase;
  }
  .mark-circle {
    position: absolute; left: 62px; top: 140px;
    width: 52px; height: 52px; border-radius: 50%;
    border: 4px solid var(--white);
  }
  .contact-list {
    position: absolute; left: 196px; top: 186px;
    list-style: none; color: var(--white);
    font-weight: 500; font-size: 12px; letter-spacing: 3px;
    line-height: 1.45; text-transform: uppercase;
  }
  .contact-list .gap { margin-top: 10px; }

  /* Company side */
  .card--company { left: 625px; background: var(--paper); }
  .brand {
    position: absolute; left: 0; right: 0; top: 110px;
    display: flex; align-items: center; justify-content: center; gap: 14px;
  }
  .brand__dot {
    width: 40px; height: 40px; border-radius: 50%;
    background: var(--brand-red);
  }
  .brand__name {
    color: var(--brand-red); font-weight: 700; font-size: 28px;
    letter-spacing: 3px; text-transform: uppercase;
  }
  .company-address {
    position: absolute; left: 36px; bottom: 36px;
    color: var(--ink-grey); font-weight: 500; font-size: 10px;
    letter-spacing: 2.5px; text-transform: uppercase;
  }
</style>
</head>
<body>

  <section class="card card--personal" aria-label="Personal side">
    <svg class="card__shape" viewBox="0 0 520 297" preserveAspectRatio="none" aria-hidden="true">
      <path d="M0 0 H396 C470 62 512 170 510 297 H0 Z" fill="#bf2632"/>
      <path d="M396 0 C470 62 512 170 510 297" fill="none" stroke="#ffffff" stroke-width="6"/>
    </svg>
    <h1 class="person-name">Marcus<br>Delaney</h1>
    <p class="person-role">Manager</p>
    <div class="mark-circle" aria-hidden="true"></div>
    <ul class="contact-list">
      <li>Mob: 555 204 1187</li>
      <li>Ph: 555 204 1187</li>
      <li class="gap">marcus@kestrel.com</li>
      <li>www.kestrel.com</li>
    </ul>
  </section>

  <section class="card card--company" aria-label="Company side">
    <div class="brand">
      <span class="brand__dot" aria-hidden="true"></span>
      <span class="brand__name">Kestrel Trading</span>
    </div>
    <p class="company-address">24 Harbor Lane, Milford, TN 37040</p>
  </section>

</body>
</html>
```